I want to sell a virtual ticket that captures customers details.

Using this information, i manually write the customers details on a piece of paper and enter them into a draw/raffle to potentially win a watch. I dont need random generators/software to pick winners, as law mandates this process to be physically done. All i need is a nice website that allows customers to purchase and enter. I have posted a few links below in the description. If you refer to brightcanoparade.com, you will see what i am after. I have my own site www.themarbleparlourhouse.com.au but i dont like how it looks and i want something better. I hope this will give you an idea on what i am after.

Target Market(s)

adults aged approximately 24-56

Industry/Entity Type

luxury watches / contestant giveaways

Number of Pages Required

4 page

Font styles to use
Serif
Other font styles liked:
• something classy - i am not sure

Colors

Designer to choose only greyscale colors for use in the design.

Requirements
Must have
• Stripe payment software

```html
<!DOCTYPE html>
<html lang="en">
<head>
<meta charset="utf-8">
<title>The Velour Assembly — Watch Competitions</title>
<link rel="stylesheet" href="https://fonts.googleapis.com/css2?family=Cinzel:wght@400;500;600&family=Playfair+Display:wght@400;600&family=Questrial&display=swap">
<style>
:root{
  --ink:#1f1f24;
  --navy:#23222e;
  --gold:#efdf8f;
  --gold-line:#e7d37a;
  --paper:#ffffff;
  --mist:#f7f7f7;
  --fog:#f1f1f1;
  --stone:#dcdbde;
  --muted:#6b6b70;
  --rule:#cfcfcf;
}
*{box-sizing:border-box;margin:0;padding:0}
html,body{width:1200px;height:3686px;overflow:hidden;background:var(--paper)}
body{position:relative;font-family:"Questrial",Arial,sans-serif;color:var(--ink)}
.abs{position:absolute}
.display{font-family:"Cinzel",Georgia,serif;font-weight:400;letter-spacing:2px}
.vline{position:absolute;width:2px;background:var(--gold-line)}
.vline.grey{background:#bdbdbd;width:1px}
.btn{position:absolute;background:var(--gold);border-radius:30px;font-size:11px;letter-spacing:.5px;display:flex;align-items:center;justify-content:center;color:var(--ink)}

/* header */
.hero-bg{left:0;top:0;width:1200px;height:705px;background:var(--mist)}
.brand{left:0;width:1200px;top:22px;text-align:center}
.brand-mark{display:inline-block;width:30px;height:30px;background:var(--ink);margin-bottom:8px}
.brand-name{font-size:13px;letter-spacing:2px;color:var(--ink)}
.menu{left:1023px;top:45px;font-size:14px;display:flex;align-items:center;gap:12px}
.menu svg{display:block}

/* hero */
.hero-photo{left:345px;top:97px;width:767px;height:533px;background:linear-gradient(160deg,#e1e0e4 0%,#d6d5da 55%,#c9c8cc 100%)}
.hero-frame{left:985px;top:549px;width:142px;height:111px;border:2px solid var(--gold-line);border-left:none;border-top:none}
.hero-title{left:92px;top:228px;font-size:50px;line-height:58px;letter-spacing:3px}
.hero-title span{display:block;font-size:55px}
.hero-sub{left:95px;top:356px;width:360px;font-size:13px;line-height:17px}
.ticket{left:92px;top:478px;width:413px;height:152px;background:var(--gold);border-radius:0 60px 0 34px}
.countdown{left:92px;top:478px;width:318px;height:70px;background:var(--navy);display:flex;align-items:center;justify-content:space-around;color:#fff}
.countdown div{text-align:center;font-family:"Playfair Display",serif;font-size:17px;line-height:17px;padding:0 14px;border-right:1px solid #4a4958}
.countdown div:last-child{border-right:none}
.countdown small{display:block;font-size:10px;letter-spacing:1px;margin-top:2px}
.left-count{left:410px;top:491px;width:73px;text-align:center;font-family:"Playfair Display",serif;font-size:9px;line-height:11px}
.left-count b{display:block;font-size:16px;font-weight:400;line-height:18px}
.comp-name{left:124px;top:572px;width:200px;font-family:"Playfair Display",serif;font-size:14px;line-height:18px;letter-spacing:.3px}
.comp-cta{left:330px;top:582px;font-family:"Playfair Display",serif;font-size:12px;font-weight:600;display:flex;align-items:center;gap:6px;white-space:nowrap}

/* packages */
.section-title{width:1200px;left:0;text-align:center;font-size:30px;letter-spacing:2px}
.pkg{position:absolute;background:#fff;border:1px solid #d8d8d8;text-align:center}
.pkg.featured{border:none;box-shadow:0 4px 26px rgba(0,0,0,.12)}
.pkg h4{font-weight:400;font-size:12px;letter-spacing:.5px}
.pkg .price{font-size:42px;letter-spacing:1px;margin:10px 0 8px;line-height:50px}
.pkg p{font-size:13px;line-height:20px;letter-spacing:.3px}
.pkg .btn{position:relative;display:flex;margin:18px auto 0;width:124px;height:34px}

/* about */
.about-bg{left:0;top:1230px;width:1200px;height:700px;background:linear-gradient(#f2f2f2 0%,#f2f2f2 80%,#fff 100%)}
.about-photo{left:150px;top:1360px;width:295px;height:360px;background:linear-gradient(150deg,#e4e2dc 0%,#d9d2b8 50%,#e6e4de 100%)}
.who{left:590px;top:1352px;font-size:34px;letter-spacing:2px}
.who b{font-weight:600}
.who-text{left:594px;top:1410px;width:500px;font-size:15px;line-height:23px;color:#444}
.values-h{left:592px;top:1500px;font-size:17px;font-weight:400}
.values-h b{font-weight:700}
.value{position:absolute;width:240px}
.value svg{position:absolute;left:0;top:0}
.value h5{margin-left:62px;font-size:13px;font-weight:700;letter-spacing:.5px}
.value p{margin-left:64px;margin-top:10px;font-size:11px;line-height:17px;color:var(--muted)}

.box{position:absolute;top:1823px;width:323px;height:215px;padding:10px}
.box-in{width:100%;height:100%;border:1px solid #bbb;padding:22px 34px}
.box h3{font-size:21px;font-weight:400;letter-spacing:1.5px;margin-top:18px}
.box h3 b{font-weight:700}
.box p{font-size:12px;line-height:20px;margin-top:8px;color:#444}
.box.mission{left:113px;background:#fff;box-shadow:0 2px 12px rgba(0,0,0,.06)}
.box.vision{left:454px;background:linear-gradient(135deg,#1e1e1f,#2b2b2d 40%,#161617 70%,#262628);color:#fff}
.box.vision .box-in{border-color:#555}
.box.vision p{color:#ddd}
.box.purpose{left:788px;background:var(--gold)}
.box.purpose .box-in{border-color:#d5c168}

/* process */
.eyebrow{left:0;width:1200px;text-align:center;top:2095px;font-size:13px;letter-spacing:2px;color:#555}
.how{top:2120px;font-size:38px}
.step-circle{position:absolute;left:544px;width:116px;height:116px;border-radius:50%;background:#fff;border:1px solid #ddd}
.arc{position:absolute;left:538px;width:128px;height:128px}
.step-text{position:absolute;width:330px}
.step-text h6{font-size:12px;font-weight:700;letter-spacing:.5px}
.step-text h4{font-size:16px;font-weight:400;margin-top:14px;letter-spacing:.3px}
.step-text p{font-size:10px;line-height:17px;color:var(--muted);margin-top:12px}
.step-text.right{text-align:right}

/* cta band */
.cta{left:0;top:2933px;width:1200px;height:373px;background:radial-gradient(ellipse at 70% 55%,#6c6c6c 0%,#3a3a3a 40%,#1e1e1e 80%),#2a2a2a}
.cta-title{left:0;width:1200px;top:3055px;text-align:center;color:#fff;font-size:42px;letter-spacing:3px}
.cta-text{left:310px;width:580px;top:3108px;text-align:center;color:#eee;font-size:13px;line-height:24px}

/* footer */
.foot-h{font-size:18px;letter-spacing:.5px;font-weight:400}
.foot-h::after{content:"";display:block;width:34px;height:2px;background:var(--gold-line);margin-top:12px}
.foot-list{font-size:11px;line-height:27px;letter-spacing:.5px;list-style:none}
.foot-div{position:absolute;top:3372px;width:1px;height:178px;background:#ddd}
.email{left:848px;top:3442px;width:245px;height:34px;background:#f1f1f1;border-radius:20px;font-size:10px;padding-left:18px;display:flex;align-items:center;color:#555}
.copyright{left:0;width:1200px;top:3645px;text-align:center;font-size:11px;letter-spacing:.4px}
</style>
</head>
<body>

<div class="abs hero-bg"></div>
<header>
  <div class="abs brand"><span class="brand-mark"></span><div class="brand-name">THE VELOUR ASSEMBLY</div></div>
  <div class="abs menu">Menu
    <svg width="26" height="16" viewBox="0 0 26 16"><path d="M0 1h26M0 8h26M4 15h22" stroke="#1f1f24" stroke-width="1.4"/></svg>
  </div>
</header>

<div class="abs hero-photo" role="img" aria-label="Three luxury dive and chronograph watches standing on white plinths against a soft grey backdrop"></div>
<div class="abs hero-frame"></div>

<h1 class="abs hero-title display">THE VELOUR<span>COLLECTION</span></h1>
<p class="abs hero-sub">To create a community where all members can feel a sense of belongingness with another</p>

<div class="abs ticket"></div>
<div class="abs countdown">
  <div>0<small>DAYS</small></div>
  <div>05<small>HOURS</small></div>
  <div>08<small>MIN</small></div>
  <div>28<small>SEC</small></div>
</div>
<div class="abs left-count">ONLY<b>44</b>TICKETS LEFT</div>
<p class="abs comp-name">CORSAIR, NIGHTBIRD &amp;<br>AMBER COMP</p>
<div class="abs comp-cta">ENTER COMPETITION
  <svg width="16" height="10" viewBox="0 0 16 10"><path d="M0 5h15M11 1l4 4-4 4" fill="none" stroke="#1f1f24" stroke-width="1.2"/></svg>
</div>

<div class="vline grey" style="left:595px;top:672px;height:53px"></div>

<h2 class="abs section-title display" style="top:755px"><b style="font-weight:600">MEMBERSHIP</b> PACKAGES</h2>

<div class="pkg" style="left:130px;top:865px;width:295px;height:271px;padding-top:36px">
  <h4>ENTRY</h4><div class="price">6.99</div>
  <p>BUYS YOU A<br>MEMBERSHIP + ONE ENTRY<br>TO THE MARQUEE .. DRAW</p>
  <span class="btn">GET STARTED</span>
</div>
<div class="pkg featured" style="left:435px;top:838px;width:317px;height:316px;padding-top:52px">
  <h4>TWO ENTRY</h4><div class="price">10.99</div>
  <p>BUYS YOU A<br>MEMBERSHIP + TWO ENTRY<br>TO THE MARQUEE .. DRAW</p>
  <span class="btn">GET STARTED</span>
</div>
<div class="pkg" style="left:763px;top:865px;width:294px;height:271px;padding-top:31px">
  <h4>THREE ENTRY</h4><div class="price">15</div>
  <p>BUYS YOU A<br>MEMBERSHIP + THREE ENTRY<br>TO THE MARQUEE .. DRAW</p>
  <span class="btn">GET STARTED</span>
</div>

<div class="abs about-bg"></div>
<div class="vline" style="left:597px;top:1205px;height:53px"></div>
<div class="abs about-photo" role="img" aria-label="Gold and black chronograph wristwatch with a metal bracelet"></div>

<h2 class="abs who display">WHO <b>WE ARE</b></h2>
<p class="abs who-text">A 100% Australian owned company whose main goal is to create a community for people who love what we love – luxury watches!</p>
<h3 class="abs values-h">OUR <b>VALUES</b></h3>

<div class="value" style="left:593px;top:1547px">
  <svg width="46" height="46" viewBox="0 0 46 46" fill="none" stroke="#444" stroke-width="1.2"><circle cx="23" cy="17" r="12"/><circle cx="23" cy="17" r="7"/><path d="M15 27l-6 14 6-3 3 5 4-11M31 27l6 14-6-3-3 5-4-11"/></svg>
  <h5>LOYALTY</h5><p>We always have our customers and the community at the heart of what we do.</p>
</div>
<div class="value" style="left:857px;top:1558px">
  <svg width="52" height="46" viewBox="0 0 52 46" fill="none" stroke="#444" stroke-width="1.2"><rect x="2" y="16" width="8" height="22"/><path d="M10 20h8l10-12 4 2-5 10h16c3 0 3 5 0 5h-4c3 0 3 5 0 5h-3c3 0 3 5 0 5H10"/></svg>
  <h5 style="margin-left:68px">TRUST</h5><p style="margin-left:68px;margin-top:8px">We're open and honest.</p>
</div>
<div class="value" style="left:598px;top:1660px">
  <svg width="50" height="44" viewBox="0 0 50 44" fill="none" stroke="#444" stroke-width="1.2"><path d="M25 40L6 22C-2 13 8 0 18 7l7 6 7-6c10-7 20 6 12 15z"/><path d="M14 26l6-5 5 4 5-4M18 30l5-4M22 34l4-4"/></svg>
  <h5>RESPECT</h5><p>We do what we say and say what we do.</p>
</div>
<div class="value" style="left:857px;top:1660px">
  <svg width="48" height="48" viewBox="0 0 48 48" fill="none" stroke="#444" stroke-width="1.2"><circle cx="24" cy="24" r="20" stroke-dasharray="3 3"/><path d="M24 12v12l8 5"/></svg>
  <h5 style="margin-left:68px">COMMITMENT</h5><p style="margin-left:68px">We ensure that we dedicate our time to deliver the best experience for you.</p>
</div>

<div class="box mission"><div class="box-in">
  <svg width="40" height="38" viewBox="0 0 40 38" fill="none" stroke="#333" stroke-width="1.3"><path d="M2 36L16 12l6 9 5-6 11 21z M16 12V2l9 3-9 3"/></svg>
  <h3>OUR <b>MISSION</b></h3>
  <p>To create a community where all members can feel a sense of belonging with another. Our mission</p>
</div></div>
<div class="box vision" role="img" aria-label="Dark marble texture panel"><div class="box-in">
  <svg width="40" height="34" viewBox="0 0 40 34" fill="none" stroke="#fff" stroke-width="1.3"><path d="M2 20c10-12 26-12 36 0-10 12-26 12-36 0z"/><circle cx="20" cy="20" r="6"/><path d="M20 2v6M10 5l3 5M30 5l-3 5"/></svg>
  <h3>OUR <b>VISION</b></h3>
  <p>To help</p>
</div></div>
<div class="box purpose"><div class="box-in">
  <svg width="34" height="40" viewBox="0 0 34 40" fill="none" stroke="#333" stroke-width="1.3"><path d="M17 38V20M17 26l-5-4M17 23l5-4"/><path d="M9 24C2 22 2 12 8 10c0-7 12-9 15-3 7 0 9 10 3 13-2 4-9 5-17 4z"/></svg>
  <h3>OUR <b>PURPOSE</b></h3>
  <p>Help us rebuild Australia one<br>tree at a time.</p>
</div></div>

<p class="abs eyebrow">OUR PROCESS</p>
<h2 class="abs section-title display how">HOW TO PLAY</h2>
<div class="vline" style="left:601px;top:2178px;height:58px"></div>
<div class="vline" style="left:602px;top:2380px;height:520px"></div>

<svg class="arc" style="top:2254px" viewBox="0 0 128 128"><path d="M64 2A62 62 0 0 1 64 126" fill="none" stroke="#e7d37a" stroke-width="5"/></svg>
<div class="step-circle" style="top:2260px">
  <svg width="116" height="116" viewBox="0 0 116 116" fill="none" stroke="#444" stroke-width="1.3"><path d="M34 46h48v8a4 4 0 0 0 0 8v8H34v-8a4 4 0 0 0 0-8z"/><path d="M42 52h18M42 58h22M42 64h14M68 48v20"/></svg>
</div>
<div class="step-text" style="left:684px;top:2268px"><h6>STEP 1</h6><h4>Pick a package.</h4>
  <p>Lorem Ipsum is simply dummy text of the printing and typesetting industry. Lorem Ipsum has been the industry's standard dummy text ever since the 1500s, when an unknown printer</p></div>

<svg class="arc" style="top:2444px" viewBox="0 0 128 128"><path d="M64 2A62 62 0 0 0 64 126" fill="none" stroke="#b8b8b8" stroke-width="5"/></svg>
<div class="step-circle" style="top:2450px">
  <svg width="116" height="116" viewBox="0 0 116 116" fill="none" stroke="#444" stroke-width="1.3"><path d="M42 40h32v36H42z"/><path d="M48 50h20M48 56h20M48 62h20M48 68h14"/></svg>
</div>
<div class="step-text right" style="left:175px;top:2456px"><h6>STEP 2</h6><h4 style="margin-top:12px">Enter Details</h4>
  <p>Lorem Ipsum is simply dummy text of the printing and typesetting industry. Lorem Ipsum has been the industry's standard dummy text ever since the 1500s, when an unknown printer</p></div>

<svg class="arc" style="top:2634px" viewBox="0 0 128 128"><path d="M64 2A62 62 0 0 1 64 126" fill="none" stroke="#e7d37a" stroke-width="5"/></svg>
<div class="step-circle" style="top:2640px">
  <svg width="116" height="116" viewBox="0 0 116 116" fill="none" stroke="#444" stroke-width="1.3"><circle cx="58" cy="58" r="14"/><path d="M58 49l3 6 6 1-4 4 1 6-6-3-6 3 1-6-4-4 6-1z"/><path d="M40 66l-4 8h44l-4-8M46 40l-3-4M70 40l3-4M58 36v-5"/></svg>
</div>
<div class="step-text" style="left:684px;top:2650px"><h6>STEP 3</h6><h4>Wait for draw its that simple!</h4>
  <p>Lorem Ipsum is simply dummy text of the printing and typesetting industry. Lorem Ipsum has been the industry's standard dummy text ever since the 1500s, when an unknown printer</p></div>

<div class="abs cta" role="img" aria-label="Black and white close-up of a wristwatch worn on a wrist"></div>
<div class="vline" style="left:607px;top:2895px;height:90px"></div>
<h2 class="abs cta-title display">GET START COMPETITION</h2>
<p class="abs cta-text">Lorem Ipsum is simply dummy text of the printing and typesetting industry. Lorem Ipsum has been the industry's standard dummy text ever</p>
<span class="btn" style="left:505px;top:3212px;width:207px;height:44px;font-size:12px">ENTER COMPETITION</span>

<footer>
  <div class="abs" style="left:210px;top:3375px">
    <h4 class="foot-h">QUICK LINKS</h4>
    <ul class="foot-list" style="margin-top:16px"><li>ABOUT US</li><li>FAQS</li><li>CONTACT US</li><li>TERMS &amp; CONDITIONS</li></ul>
  </div>
  <div class="foot-div" style="left:420px"></div>
  <div class="abs" style="left:505px;top:3375px">
    <h4 class="foot-h">CONTACT US</h4>
    <div class="foot-list" style="line-height:17px;margin-top:16px">
      <p style="font-weight:700">ADDRESS</p>
      <p>14 HARLOW LANE WESTMERE<br>VIC 3099.</p>
      <p style="margin-top:12px">INFO@THEVELOURASSEMBLY.COM.AU</p>
      <p style="margin-top:14px">0400 123 456.</p>
    </div>
  </div>
  <div class="foot-div" style="left:778px"></div>
  <div class="abs" style="left:848px;top:3382px">
    <h4 class="foot-h">SUBSCRIBE EMAIL</h4>
  </div>
  <div class="abs email">YOUR EMAIL</div>
  <span class="btn" style="left:855px;top:3488px;width:236px;height:36px">SUBSCRIBE NOW</span>
  <p class="abs copyright">COPYRIGHT © 2021 THE VELOUR ASSEMBLY</p>
</footer>

</body>
</html>
```